Professional Single Page Website Design for Velloway Advisory

Velloway Advisory is a new business consultancy specializing in providing expert services to small businesses, primarily in the brick-and-mortar retail and food service sectors. We offer a range of services including franchise development and launch, due diligence, and construction management.

Currently, we have a basic website set up at www.vellowayadvisory.example, but we need a professional touch to enhance its design and functionality.

Project Requirements:
- Single Page Design: For now, we need a single page design that effectively showcases who we are, our services, and contact information.
- Future Expansion: The design should be flexible and scalable for future expansion to include additional pages like specific service offerings, about us, and a dedicated contact page.
- Design Aesthetic: We are looking for a modern yet professional design that aligns with our brand identity.
- Logo: We have a logo that we like, which was also sourced from Pixel Forum. The logo files are attached to this project brief.

Key Sections to Include:
- Hero Section: An engaging introduction to Velloway Advisory with a strong visual impact.
- About Us: A brief overview of who we are and our mission.
- Team: Section for the profiles of the two principals.
- Services: A clear and concise presentation of our services, including franchise development, due diligence, and construction management.
- Contact Information: Easy-to-find contact details, including a form for inquiries.
- Call to Action: Encouraging visitors to get in touch with us for consultations or further information.

Design Considerations:
- Ensure the design is responsive and mobile-friendly.
- Include high-quality images and icons that complement our services and industry.
- We do not need development services, this is only a design project.

```html
<!DOCTYPE html>
<html lang="en">
<head>
<meta charset="utf-8">
<title>Velloway Advisory — Single Page Website</title>
<link href="https://fonts.googleapis.com/css2?family=Poppins:wght@400;500;600;700;800&display=swap" rel="stylesheet">
<style>
:root{
  --board:#b3c8dd;
  --green:#93c6ab;
  --green-deep:#6a9c82;
  --green-text:#8cc3a6;
  --ink:#1c2127;
  --dark:#262b33;
  --dark-deep:#1e242b;
  --muted:#6d7176;
  --line:#e4e6e8;
  --soft:#f3f4f4;
  --white:#ffffff;
}
*{box-sizing:border-box;margin:0;padding:0}
html,body{width:1200px;height:2662px;overflow:hidden}
body{background:var(--board);font-family:"Poppins",sans-serif;color:var(--ink)}
.page{position:absolute;top:49px;width:562px;height:2558px;background:var(--white);overflow:hidden}
.page--plain{left:27px}
.page--modal{left:606px}
section,footer{position:relative;width:562px}
.abs{position:absolute}
.eyebrow{position:absolute;font-size:5.5px;font-weight:500;letter-spacing:.3px;color:var(--green-text);text-transform:uppercase}
.h2{position:absolute;font-weight:700;font-size:21px;line-height:24px;color:var(--ink)}
.body{font-size:5.6px;line-height:10.4px;color:#444a50}
.tick{position:absolute;background:#8a8f94}

/* hero */
.hero{height:346px;background:linear-gradient(160deg,#3c4a5c 0%,#2b3645 45%,#1f2a36 100%);color:var(--white)}
.hero__photo{position:absolute;inset:0;background:linear-gradient(180deg,rgba(88,104,128,.55),rgba(30,38,48,.3) 60%,rgba(44,64,46,.55))}
.brand{position:absolute;left:35px;top:22px;display:flex;align-items:center;gap:6px;font-weight:600;font-size:10px;color:var(--white)}
.brand__dot{width:28px;height:28px;border-radius:50%;border:3px solid var(--green)}
.nav{position:absolute;right:33px;top:22px;display:flex;gap:4px;font-size:6.5px;font-weight:500}
.nav span{padding:3px 6px;border-radius:2px}
.nav .is-active{background:var(--green)}
.hero__title{position:absolute;left:34px;top:96px;font-size:21.5px;line-height:24px;font-weight:800}
.hero__sub{position:absolute;left:34px;top:150px;font-size:14px;line-height:19px;font-weight:700}
.hero__text{position:absolute;left:34px;top:196px;width:240px;font-size:5.8px;line-height:10.8px}
.btn-green{position:absolute;background:var(--green);color:var(--white);font-size:6.5px;font-weight:500;text-align:center;border-radius:1px}
.hero .btn-green{left:34px;top:276px;width:70px;height:18px;line-height:18px}
.mouse{position:absolute;left:275px;top:306px;width:12px;height:19px;border:1.5px solid var(--white);border-radius:7px}

/* about */
.about{height:284px}
.about .tick{left:0;top:42px;width:28px;height:1px}
.about .eyebrow{left:35px;top:39px}
.about .h2{left:35px;top:50px}
.about__text{position:absolute;left:35px;top:108px;width:200px;text-align:justify}
.about__text p+p{margin-top:7px}
.photo{position:absolute}
.ph-building-a{left:245px;top:36px;width:140px;height:98px;background:linear-gradient(180deg,#6fa0d6,#cbd6df 60%,#7d8b92)}
.ph-building-b{left:245px;top:137px;width:140px;height:96px;background:linear-gradient(180deg,#8fb6e0,#dfe3e6 55%,#585f66)}
.ph-engineers{left:390px;top:58px;width:139px;height:153px;background:linear-gradient(160deg,#9c8b71,#565548 50%,#d8d1b0)}

/* team */
.team{height:355px;background:var(--soft)}
.team .tick{left:280px;top:0;width:1px;height:22px}
.team .eyebrow{left:0;width:562px;text-align:center;top:30px}
.team .h2{left:0;width:562px;text-align:center;top:44px;font-size:20px}
.card{position:absolute;top:134px;width:240px;height:181px;text-align:center;color:var(--white)}
.card--green{left:35px;background:var(--green)}
.card--dark{left:288px;background:var(--dark)}
.diamond{position:absolute;width:76px;height:76px;transform:rotate(45deg);border-radius:8px;overflow:hidden}
.team .diamond{top:94px}
.d-left{left:117px;background:radial-gradient(circle at 50% 45%,#c59a7c,#6b4a3a 70%)}
.d-right{left:370px;background:radial-gradient(circle at 50% 45%,#d3a588,#8fa9c0 70%)}
.card__name{position:absolute;top:66px;left:0;width:100%;font-size:12px;font-weight:700}
.card__role{position:absolute;top:83px;left:0;width:100%;font-size:7px;font-weight:600}
.card--dark .card__role{color:var(--green)}
.card__text{position:absolute;top:98px;left:12px;right:12px;font-size:5.3px;line-height:10.2px}
.card--green .card__text{color:#eef6f1}
.card__btn{position:absolute;top:137px;left:85px;width:70px;height:19px;line-height:17px;border:1px solid var(--white);font-size:6.5px}

/* services */
.services{height:465px}
.services .tick{left:0;top:42px;width:28px;height:1px}
.services .eyebrow{left:35px;top:38px}
.services .h2{left:35px;top:48px;font-size:20px}
.svc{position:absolute;width:154px;height:110px;background:var(--soft);text-align:center;padding:10px 8px 0}
.svc__icon{width:26px;height:24px;margin:0 auto 5px;border:1.5px solid #3b4148;border-radius:2px}
.svc__title{font-size:9.5px;line-height:13px;font-weight:600}
.svc__text{margin-top:4px;font-size:5.3px;line-height:9.6px;color:var(--muted)}
.svc--green{background:var(--green);color:var(--white)}
.svc--green .svc__icon{border-color:var(--white)}
.svc--green .svc__text{color:#eef6f1}
.feature{position:absolute;left:205px;top:217px;width:323px;height:233px;border:1px solid var(--line)}
.feature__title{position:absolute;left:9px;top:8px;width:150px;font-size:17px;line-height:21px;font-weight:700;color:var(--green-text)}
.feature__lead{position:absolute;left:9px;top:76px;width:136px;font-size:5.5px;line-height:11px;color:#4a5056}
.feature__photo{position:absolute;left:160px;top:10px;width:152px;height:137px;background:linear-gradient(150deg,#4b5b6a,#a4a07e 55%,#d8dbd4)}
.feature__text{position:absolute;left:9px;top:158px;width:305px;font-size:5.5px;line-height:11px;color:#4a5056}

/* cta */
.cta{height:271px}
.cta__box{position:absolute;left:35px;top:23px;width:493px;height:209px;background:linear-gradient(135deg,#78a88d,#5e9278);text-align:center;color:var(--white)}
.cta__title{margin-top:40px;font-size:20px;line-height:24px;font-weight:700}
.cta__text{margin-top:7px;font-size:6.3px;line-height:13px;color:#eaf4ee}
.cta__btn{display:inline-block;margin-top:10px;padding:0 11px;height:20px;line-height:20px;background:var(--dark);font-size:6.5px;font-weight:500}

/* contact */
.contact{height:310px;background:linear-gradient(110deg,#262c34,#1e242b 55%,#2a3038)}
.contact .tick{left:280px;top:0;width:1px;height:20px;background:#c9ccd0}
.contact .eyebrow{left:0;width:562px;text-align:center;top:28px}
.contact .h2{left:0;width:562px;text-align:center;top:41px;color:var(--white);font-size:20px}
.field{position:absolute;height:22px;background:var(--white);font-size:5.6px;color:#444;padding:7px 8px}
.contact .btn-green{left:245px;top:247px;width:72px;height:20px;line-height:20px}

/* location */
.location{height:127px;text-align:center}
.location .tick{left:280px;top:0;width:1px;height:20px}
.location .eyebrow{left:0;width:562px;top:28px}
.location .h2{left:0;width:562px;top:41px;font-size:20px}
.loc__name{position:absolute;left:0;width:562px;top:79px;font-size:12.5px;font-weight:700}
.loc__name span{color:var(--green-text)}
.loc__addr{position:absolute;left:0;width:562px;top:103px;font-size:7px;display:flex;justify-content:center;gap:5px;align-items:center}
.map{height:205px;background:linear-gradient(120deg,#e6ebe4,#eef0ee 40%,#dfe6ea 70%,#e9ece6)}

/* footer */
.footer{height:155px}
.footer__brand{position:absolute;left:35px;top:44px;width:100px;text-align:center;font-size:10.5px;font-weight:600}
.footer__brand .brand__dot{width:54px;height:54px;border-width:5px;margin:0 auto 10px}
.col{position:absolute;top:32px;font-size:6px;line-height:16px}
.col h4{font-size:7.5px;font-weight:600;color:var(--green-text);margin-bottom:3px;line-height:14px}
.news p{font-size:5.8px;line-height:10px;width:112px}
.news__email{margin-top:6px;width:113px;height:19px;border:1px solid #cfd3d6;font-size:5.8px;padding:5px 7px}
.news__btn{margin-top:8px;width:113px;height:20px;background:var(--dark);color:var(--white);font-size:6.5px;font-weight:600;text-align:center;line-height:20px}
.copy{height:40px;border-top:1px solid var(--line)}
.copy__text{position:absolute;left:35px;top:17px;font-size:5.2px;color:#555}
.copy__text span{color:var(--green-text)}
.socials{position:absolute;right:34px;top:11px;display:flex;gap:4px}
.socials i{width:16px;height:16px;border:1px solid #8b9095;border-radius:50%}

/* modal state */
.dim{position:absolute;inset:0;background:rgba(20,22,26,.46)}
.modal{position:absolute;left:77px;top:742px;width:409px;height:178px;background:var(--white);box-shadow:0 4px 16px rgba(0,0,0,.25)}
.modal .diamond{left:45px;top:42px;width:94px;height:94px;background:radial-gradient(circle at 50% 45%,#c59a7c,#6b4a3a 70%)}
.modal__name{position:absolute;left:154px;top:12px;font-size:12px;font-weight:600;color:var(--green-text)}
.modal__role{position:absolute;left:154px;top:31px;font-size:7px;font-weight:600}
.modal__text{position:absolute;left:154px;top:44px;width:244px;font-size:5.5px;line-height:10.8px;color:#3e444a}
.modal__text p+p{margin-top:5px}
.modal__links{position:absolute;left:154px;top:154px;display:flex;gap:14px;font-size:6.5px;font-weight:600;align-items:center}
.modal__links i{display:inline-block;width:6px;height:6px;background:var(--green);margin-right:4px;border-radius:1px}
.modal__close{position:absolute;right:6px;top:6px;width:13px;height:13px;border:1px solid #888;border-radius:50%;font-size:7px;line-height:11px;text-align:center}
</style>
</head>
<body>

<!-- Page: default state -->
<div class="page page--plain">
  <section class="hero">
    <div class="hero__photo" role="img" aria-label="Photo of a modern commercial office building at dusk"></div>
    <div class="brand"><span class="brand__dot"></span>Velloway Advisory</div>
    <nav class="nav"><span class="is-active">Home</span><span>About</span><span>Services</span><span>Team</span><span>Contact</span></nav>
    <h1 class="hero__title">Building Success<br>in Southern California</h1>
    <p class="hero__sub">Expertise at Every Step:<br>From Planning to Execution</p>
    <p class="hero__text">At Velloway, we blend innovative strategies with local market expertise to guide your commercial real estate ventures. Whether you're launching a new restaurant, investing in retail spaces, or expanding a franchise, our dedicated team is here to turn your real estate aspirations into tangible success. Dive into a partnership that grows with you.</p>
    <div class="btn-green">Read More</div>
    <div class="mouse"></div>
  </section>

  <section class="about">
    <div class="tick"></div>
    <div class="eyebrow">Welcome</div>
    <h2 class="h2">About Velloway<br>Advisory</h2>
    <div class="about__text body">
      <p>Welcome to Velloway Advisory, your trusted partner in navigating the complexities of the real estate and small business markets. Founded by industry veterans Mateo Reyes and Daniel Oh, we specialize in providing comprehensive services tailored to the unique needs of our clients. Whether you're a franchisee, a new restaurant owner, or a commercial real estate investor, our expertise in due diligence, construction management, and investment property evaluation ensures you make informed, strategic decisions.</p>
      <p>At Velloway Advisory, we are committed to your success. Our approach combines meticulous analysis, strategic insights, and personalized service to help you achieve your business goals.</p>
    </div>
    <div class="photo ph-building-a" role="img" aria-label="Photo of a modern office building"></div>
    <div class="photo ph-building-b" role="img" aria-label="Photo of a retail storefront building"></div>
    <div class="photo ph-engineers" role="img" aria-label="Photo of two engineers in hard hats reviewing plans"></div>
  </section>

  <section class="team">
    <div class="tick"></div>
    <div class="eyebrow">Our Leadership Team</div>
    <h2 class="h2">Meet Our Team</h2>
    <div class="card card--green">
      <div class="card__name">Daniel Oh</div>
      <div class="card__role">Principal</div>
      <p class="card__text">Daniel Oh is a seasoned real estate expert with extensive experience in project and construction management, and a licensed real estate agent in California. Fluent in both English and Korean, he...</p>
      <div class="card__btn">Contact Us</div>
    </div>
    <div class="card card--dark">
      <div class="card__name">Mateo Reyes</div>
      <div class="card__role">Principal</div>
      <p class="card__text">Mateo Reyes brings almost 20 years of rich experience as a real estate investor and a pivotal role at one of southern California's largest real estate management firms, where he...</p>
      <div class="card__btn">Contact Us</div>
    </div>
    <div class="diamond d-left" role="img" aria-label="Portrait of Daniel Oh"></div>
    <div class="diamond d-right" role="img" aria-label="Portrait of Mateo Reyes"></div>
  </section>

  <section class="services">
    <div class="tick"></div>
    <div class="eyebrow">What We Do</div>
    <h2 class="h2">Our Services</h2>
    <div class="svc" style="left:35px;top:93px"><div class="svc__icon" role="img" aria-label="Franchise icon"></div><div class="svc__title">Franchise Development<br>&amp; Launch</div><p class="svc__text">Comprehensive franchise setup from evaluation to launch for scalable business growth.</p></div>
    <div class="svc" style="left:204px;top:93px"><div class="svc__icon" role="img" aria-label="Investment icon"></div><div class="svc__title">Investment Property<br>Evaluation</div><p class="svc__text">Providing detailed analysis of potential investment properties, including profitability forecasts and risk assessments.</p></div>
    <div class="svc" style="left:374px;top:93px"><div class="svc__icon" role="img" aria-label="Market analysis icon"></div><div class="svc__title">Market Analysis<br>&amp; Feasibility Studies</div><p class="svc__text">Conducting comprehensive market research to assess the viability of real estate.</p></div>
    <div class="svc" style="left:35px;top:217px"><div class="svc__icon" role="img" aria-label="Due diligence icon"></div><div class="svc__title">Due Diligence Services</div><p class="svc__text">Conducting thorough due diligence for business and property transactions to identify potential risks and liabilities.</p></div>
    <div class="svc svc--green" style="left:35px;top:340px"><div class="svc__icon" role="img" aria-label="Construction icon"></div><div class="svc__title">Building &amp; Construction Management</div><p class="svc__text">Conducting thorough due diligence for business and property transactions to identify potential risks and liabilities.</p></div>
    <div class="feature">
      <div class="feature__title">Building &amp; Construction Management</div>
      <p class="feature__lead">Our Building &amp; Construction Management Services oversee every aspect of your construction and development projects, from initial planning to final completion. We ensure projects stay on time and within budget, providing meticulous attention to detail and proactive problem-solving.</p>
      <div class="feature__photo" role="img" aria-label="Photo of a construction team reviewing blueprints on site"></div>
      <p class="feature__text">Specializing in tenant improvements (TIs) and ground-up construction for small to mid-size commercial projects, we handle everything from permitting and contractor coordination to quality control and final inspections. Trust us to deliver successful projects that meet your specifications and exceed your expectations, ensuring a smooth and efficient construction process every step of the way.</p>
    </div>
  </section>

  <section class="cta">
    <div class="cta__box" role="img" aria-label="Green-tinted aerial photo of a business park">
      <h2 class="cta__title">Unlock Your Business<br>Potential Today!</h2>
      <p class="cta__text">At Velloway Advisory, we're dedicated to turning your business aspirations into reality.<br>Our expertise and commitment ensure you make informed, strategic decisions that drive success.<br>Take the first step towards achieving your goals with confidence.</p>
      <div class="cta__btn">Get Started Now</div>
    </div>
  </section>

  <section class="contact">
    <div class="tick"></div>
    <div class="eyebrow">Get In Touch</div>
    <h2 class="h2">Contact Us</h2>
    <div class="field" style="left:119px;top:86px;width:156px">First Name</div>
    <div class="field" style="left:290px;top:86px;width:156px">Last Name</div>
    <div class="field" style="left:119px;top:116px;width:156px">Email Address</div>
    <div class="field" style="left:290px;top:116px;width:156px">Phone No</div>
    <div class="field" style="left:119px;top:147px;width:327px">Company</div>
    <div class="field" style="left:119px;top:177px;width:327px;height:64px">Message</div>
    <div class="btn-green">Submit</div>
  </section>

  <section class="location">
    <div class="tick"></div>
    <div class="eyebrow">Direction Map</div>
    <h2 class="h2">Location Address</h2>
    <div class="loc__name">Velloway <span>Advisory</span></div>
    <div class="loc__addr"><svg width="6" height="8" viewBox="0 0 6 8"><path d="M3 0a3 3 0 0 0-3 3c0 2.2 3 5 3 5s3-2.8 3-5a3 3 0 0 0-3-3z" fill="#1c2127"/><circle cx="3" cy="3" r="1" fill="#fff"/></svg>410 Harborview Dr, Lakemont, CA 90210</div>
  </section>
  <section class="map" role="img" aria-label="Street map showing the office location"></section>

  <footer class="footer">
    <div class="footer__brand"><div class="brand__dot"></div>Velloway Advisory</div>
    <div class="col" style="left:160px"><h4>Site Map</h4>Home<br>About<br>Services<br>Team<br>Contact</div>
    <div class="col" style="left:253px;line-height:15.5px"><h4>Services</h4>Franchise Development &amp; Launch<br>Due Diligence Services<br>Building &amp; Construction Management<br>Investment Property Evaluation<br>Market Analysis &amp; Feasibility Studies</div>
    <div class="col news" style="left:414px"><h4>Newsletter</h4><p>Sed ut perspiciatis unde omnis iste natus error sit.</p><div class="news__email">Email Address</div><div class="news__btn">Subscribe →</div></div>
  </footer>
  <section class="copy">
    <div class="copy__text">Copyright © 2024, <span>Velloway Advisory</span>. All Right Reserved</div>
    <div class="socials"><i></i><i></i><i></i><i></i></div>
  </section>
</div>

<!-- Page: team profile opened -->
<div class="page page--modal">
  <section class="hero">
    <div class="hero__photo" role="img" aria-label="Photo of a modern commercial office building at dusk"></div>
    <div class="brand"><span class="brand__dot"></span>Velloway Advisory</div>
    <nav class="nav"><span class="is-active">Home</span><span>About</span><span>Services</span><span>Team</span><span>Contact</span></nav>
    <h1 class="hero__title">Building Success<br>in Southern California</h1>
    <p class="hero__sub">Expertise at Every Step:<br>From Planning to Execution</p>
    <p class="hero__text">At Velloway, we blend innovative strategies with local market expertise to guide your commercial real estate ventures. Whether you're launching a new restaurant, investing in retail spaces, or expanding a franchise, our dedicated team is here to turn your real estate aspirations into tangible success. Dive into a partnership that grows with you.</p>
    <div class="btn-green">Read More</div>
    <div class="mouse"></div>
  </section>

  <section class="about">
    <div class="tick"></div>
    <div class="eyebrow">Welcome</div>
    <h2 class="h2">About Velloway<br>Advisory</h2>
    <div class="about__text body">
      <p>Welcome to Velloway Advisory, your trusted partner in navigating the complexities of the real estate and small business markets. Founded by industry veterans Mateo Reyes and Daniel Oh, we specialize in providing comprehensive services tailored to the unique needs of our clients. Whether you're a franchisee, a new restaurant owner, or a commercial real estate investor, our expertise in due diligence, construction management, and investment property evaluation ensures you make informed, strategic decisions.</p>
      <p>At Velloway Advisory, we are committed to your success. Our approach combines meticulous analysis, strategic insights, and personalized service to help you achieve your business goals.</p>
    </div>
    <div class="photo ph-building-a" role="img" aria-label="Photo of a modern office building"></div>
    <div class="photo ph-building-b" role="img" aria-label="Photo of a retail storefront building"></div>
    <div class="photo ph-engineers" role="img" aria-label="Photo of two engineers in hard hats reviewing plans"></div>
  </section>

  <section class="team">
    <div class="tick"></div>
    <div class="eyebrow">Our Leadership Team</div>
    <h2 class="h2">Meet Our Team</h2>
    <div class="card card--green">
      <div class="card__name">Daniel Oh</div>
      <div class="card__role">Principal</div>
      <p class="card__text">Daniel Oh is a seasoned real estate expert with extensive experience in project and construction management, and a licensed real estate agent in California. Fluent in both English and Korean, he...</p>
      <div class="card__btn">Contact Us</div>
    </div>
    <div class="card card--dark">
      <div class="card__name">Mateo Reyes</div>
      <div class="card__role">Principal</div>
      <p class="card__text">Mateo Reyes brings almost 20 years of rich experience as a real estate investor and a pivotal role at one of southern California's largest real estate management firms, where he...</p>
      <div class="card__btn">Contact Us</div>
    </div>
    <div class="diamond d-left" role="img" aria-label="Portrait of Daniel Oh"></div>
    <div class="diamond d-right" role="img" aria-label="Portrait of Mateo Reyes"></div>
  </section>

  <section class="services">
    <div class="tick"></div>
    <div class="eyebrow">What We Do</div>
    <h2 class="h2">Our Services</h2>
    <div class="svc" style="left:35px;top:93px"><div class="svc__icon" role="img" aria-label="Franchise icon"></div><div class="svc__title">Franchise Development<br>&amp; Launch</div><p class="svc__text">Comprehensive franchise setup from evaluation to launch for scalable business growth.</p></div>
    <div class="svc" style="left:204px;top:93px"><div class="svc__icon" role="img" aria-label="Investment icon"></div><div class="svc__title">Investment Property<br>Evaluation</div><p class="svc__text">Providing detailed analysis of potential investment properties, including profitability forecasts and risk assessments.</p></div>
    <div class="svc" style="left:374px;top:93px"><div class="svc__icon" role="img" aria-label="Market analysis icon"></div><div class="svc__title">Market Analysis<br>&amp; Feasibility Studies</div><p class="svc__text">Conducting comprehensive market research to assess the viability of real estate.</p></div>
    <div class="svc" style="left:35px;top:217px"><div class="svc__icon" role="img" aria-label="Due diligence icon"></div><div class="svc__title">Due Diligence Services</div><p class="svc__text">Conducting thorough due diligence for business and property transactions to identify potential risks and liabilities.</p></div>
    <div class="svc svc--green" style="left:35px;top:340px"><div class="svc__icon" role="img" aria-label="Construction icon"></div><div class="svc__title">Building &amp; Construction Management</div><p class="svc__text">Conducting thorough due diligence for business and property transactions to identify potential risks and liabilities.</p></div>
    <div class="feature">
      <div class="feature__title">Building &amp; Construction Management</div>
      <p class="feature__lead">Our Building &amp; Construction Management Services oversee every aspect of your construction and development projects, from initial planning to final completion. We ensure projects stay on time and within budget, providing meticulous attention to detail and proactive problem-solving.</p>
      <div class="feature__photo" role="img" aria-label="Photo of a construction team reviewing blueprints on site"></div>
      <p class="feature__text">Specializing in tenant improvements (TIs) and ground-up construction for small to mid-size commercial projects, we handle everything from permitting and contractor coordination to quality control and final inspections. Trust us to deliver successful projects that meet your specifications and exceed your expectations, ensuring a smooth and efficient construction process every step of the way.</p>
    </div>
  </section>

  <section class="cta">
    <div class="cta__box" role="img" aria-label="Green-tinted aerial photo of a business park">
      <h2 class="cta__title">Unlock Your Business<br>Potential Today!</h2>
      <p class="cta__text">At Velloway Advisory, we're dedicated to turning your business aspirations into reality.<br>Our expertise and commitment ensure you make informed, strategic decisions that drive success.<br>Take the first step towards achieving your goals with confidence.</p>
      <div class="cta__btn">Get Started Now</div>
    </div>
  </section>

  <section class="contact">
    <div class="tick"></div>
    <div class="eyebrow">Get In Touch</div>
    <h2 class="h2">Contact Us</h2>
    <div class="field" style="left:119px;top:86px;width:156px">First Name</div>
    <div class="field" style="left:290px;top:86px;width:156px">Last Name</div>
    <div class="field" style="left:119px;top:116px;width:156px">Email Address</div>
    <div class="field" style="left:290px;top:116px;width:156px">Phone No</div>
    <div class="field" style="left:119px;top:147px;width:327px">Company</div>
    <div class="field" style="left:119px;top:177px;width:327px;height:64px">Message</div>
    <div class="btn-green">Submit</div>
  </section>

  <section class="location">
    <div class="tick"></div>
    <div class="eyebrow">Direction Map</div>
    <h2 class="h2">Location Address</h2>
    <div class="loc__name">Velloway <span>Advisory</span></div>
    <div class="loc__addr"><svg width="6" height="8" viewBox="0 0 6 8"><path d="M3 0a3 3 0 0 0-3 3c0 2.2 3 5 3 5s3-2.8 3-5a3 3 0 0 0-3-3z" fill="#1c2127"/><circle cx="3" cy="3" r="1" fill="#fff"/></svg>410 Harborview Dr, Lakemont, CA 90210</div>
  </section>
  <section class="map" role="img" aria-label="Street map showing the office location"></section>

  <footer class="footer">
    <div class="footer__brand"><div class="brand__dot"></div>Velloway Advisory</div>
    <div class="col" style="left:160px"><h4>Site Map</h4>Home<br>About<br>Services<br>Team<br>Contact</div>
    <div class="col" style="left:253px;line-height:15.5px"><h4>Services</h4>Franchise Development &amp; Launch<br>Due Diligence Services<br>Building &amp; Construction Management<br>Investment Property Evaluation<br>Market Analysis &amp; Feasibility Studies</div>
    <div class="col news" style="left:414px"><h4>Newsletter</h4><p>Sed ut perspiciatis unde omnis iste natus error sit.</p><div class="news__email">Email Address</div><div class="news__btn">Subscribe →</div></div>
  </footer>
  <section class="copy">
    <div class="copy__text">Copyright © 2024, <span>Velloway Advisory</span>. All Right Reserved</div>
    <div class="socials"><i></i><i></i><i></i><i></i></div>
  </section>

  <div class="dim"></div>
  <div class="modal">
    <div class="diamond" role="img" aria-label="Portrait of Daniel Oh"></div>
    <div class="modal__name">Daniel Oh</div>
    <div class="modal__role">Principal</div>
    <div class="modal__text">
      <p>Daniel Oh is a seasoned real estate expert with extensive experience in project and construction management, and a licensed real estate agent in California. Fluent in both English and Korean, he specializes in commercial real estate, bringing invaluable expertise to Velloway Advisory.</p>
      <p>His affiliation with the National Guild of Property Brokers and the Retail Centers Alliance underscores his commitment to excellence and industry standards. Daniel's strategic insight and leadership in real estate development ensure clients receive strategic, value-driven solutions for their investments.</p>
    </div>
    <div class="modal__links"><span><i></i>Phone</span><span><i></i>Email</span></div>
    <div class="modal__close">x</div>
  </div>
</div>

</body>
</html>
```